the halvorsen group premier division

design a DL A4 tri fold brochure to reflect our creative landscape business
my web site www.thehalvorsengroup.com.au
has all the information needed
i will also be updating the website to be more updated and creative design

```html
<!DOCTYPE html>
<html lang="en">
<head>
<meta charset="utf-8">
<title>The Halvorsen Group Premier Division – Tri Fold Brochure</title>
<link rel="stylesheet" href="https://fonts.googleapis.com/css2?family=Montserrat:wght@300;400;500&family=Open+Sans:wght@400;600&display=swap">
<style>
  :root {
    --backdrop: #cfcfcf;
    --paper: #fafafa;
    --ink: #5a5a5a;
    --headline: #4a4a4a;
    --accent: #e5a13a;
    --fold: rgba(0,0,0,0.06);
    --gap: #ffffff;
  }
  * { box-sizing: border-box; margin: 0; padding: 0; }
  html, body { width: 1200px; height: 800px; overflow: hidden; }
  body {
    background: var(--backdrop);
    font-family: "Open Sans", Arial, sans-serif;
    color: var(--ink);
  }
  .brochure {
    position: absolute;
    left: 60px; top: 18px;
    width: 1080px; height: 764px;
    background: var(--paper);
    box-shadow: 0 10px 30px rgba(0,0,0,0.18);
    overflow: hidden;
  }
  .fold {
    position: absolute; top: 0; bottom: 0; width: 24px;
    background: linear-gradient(to right, transparent, var(--fold), transparent);
  }
  .fold--one { left: 348px; }
  .fold--two { left: 708px; }

  .photo { position: absolute; border: 3px solid var(--gap); }
  .photo--house-night { background: linear-gradient(160deg, #2c3a52, #6d6a55 55%, #3f5d2e); }
  .photo--grass { background: linear-gradient(170deg, #8fb56a, #4f7a34); }
  .photo--deck { background: linear-gradient(170deg, #c9a79a, #7a6552 60%, #4c3f35); }
  .photo--cushions { background: linear-gradient(170deg, #3c4a2f, #b5382f 55%, #d8d3c4); }
  .photo--pond { background: linear-gradient(160deg, #4f5b44, #7a6a4e 50%, #2f3b3a); }
  .photo--patio { background: linear-gradient(160deg, #3e4a33, #9a948a 55%, #5a5f4f); }
  .photo--entry { background: linear-gradient(160deg, #8aa3c4, #b79a6c 50%, #5b6b4a); }
  .photo--pool { background: linear-gradient(170deg, #d9dde0, #3fb0bd 60%, #a8a49a); }
  .photo--lawn { background: linear-gradient(170deg, #a7c37a, #5f9637 60%, #8e8f86); }
  .photo--garden-dusk { background: linear-gradient(170deg, #35549a, #6f8e5a 55%, #3f6d2e); }
  .photo--timber { background: linear-gradient(170deg, #e6e3dc, #c79c6a 55%, #6b5a4a); }

  .headline {
    position: absolute;
    font-family: "Montserrat", Arial, sans-serif;
    font-weight: 300;
    font-size: 30px;
    letter-spacing: 3px;
    text-transform: uppercase;
    color: var(--headline);
    white-space: nowrap;
  }
  .headline--top { left: 26px; top: 158px; }
  .headline--bottom { left: 384px; top: 558px; }

  .panel { position: absolute; width: 360px; padding: 0 26px; }
  .panel--consult { left: 0; top: 214px; }
  .panel--earthwork { left: 360px; top: 214px; }
  .panel--install { left: 720px; top: 180px; padding: 0 24px; }

  .section-title {
    font-family: "Montserrat", Arial, sans-serif;
    font-weight: 400;
    font-size: 15px;
    letter-spacing: 0.5px;
    text-transform: uppercase;
    color: var(--accent);
    margin-bottom: 10px;
  }
  .panel p {
    font-size: 12px;
    line-height: 1.45;
    text-align: justify;
    margin-bottom: 12px;
  }
  .panel--install p { margin-bottom: 9px; }
  .capabilities {
    display: grid;
    grid-template-columns: 122px 1fr;
    column-gap: 4px;
    margin: 0 0 9px;
  }
  .capabilities ul { list-style: none; }
  .capabilities li {
    font-size: 12px;
    line-height: 1.4;
    padding-left: 11px;
    position: relative;
  }
  .capabilities li::before {
    content: "";
    position: absolute; left: 1px; top: 7px;
    width: 4px; height: 4px; border-radius: 50%;
    background: var(--ink);
  }
</style>
</head>
<body>
  <main class="brochure" aria-label="The Halvorsen Group Premier Division tri fold brochure, inside spread">
    <div class="fold fold--one"></div>
    <div class="fold fold--two"></div>

    <div class="photo photo--house-night" role="img" aria-label="Formal house facade lit at dusk with clipped hedges" style="left:0;top:0;width:180px;height:150px;"></div>
    <div class="photo photo--grass" role="img" aria-label="Close view of ornamental grass planting" style="left:180px;top:0;width:180px;height:150px;"></div>
    <div class="photo photo--deck" role="img" aria-label="Timber deck with raised rendered planters" style="left:360px;top:0;width:180px;height:150px;"></div>
    <div class="photo photo--cushions" role="img" aria-label="Built-in bench seat with red cushions under a green wall" style="left:540px;top:0;width:180px;height:150px;"></div>
    <div class="photo photo--pond" role="img" aria-label="Reflective water feature in a courtyard" style="left:720px;top:0;width:165px;height:172px;"></div>
    <div class="photo photo--patio" role="img" aria-label="Paved patio with outdoor dining setting" style="left:885px;top:0;width:195px;height:172px;"></div>

    <h1 class="headline headline--top">Landscape Consulting and Design</h1>

    <section class="panel panel--consult">
      <h2 class="section-title">Consultation and Design</h2>
      <p>Our landscape designers will begin by discussing your needs and look at your property and setting to create a concept where all attributes are considered from the land itself, design style, the elements and impact, through to lifestyle, and functionality and of course budget.</p>
      <p>Whether it be new or existing, Liam Hartley can provide advice on materials, earth and irrigation, planting, features and so with only quality and longevity in mind.</p>
      <p>You may also opt for a digital interpretation of your design, at an additional cost, to help you visualise the transformation and how the design fits in with its surrounds.</p>
      <p>If you have something particular in mind or uncertain about, Liam would be happy to assist.</p>
    </section>

    <section class="panel panel--earthwork">
      <h2 class="section-title">Earthwork &amp; Site Preparation</h2>
      <p>Depending on the nature of the, it is imperative that your foundation and earth is well prepared for construction and planting. This will determine a quality outcome and the longevity we promote so you don't have issues in the future.</p>
      <p>The Halvorsen group provides the relevant services required so your ground can be covered! This includes, clearing, excavation, levelling, solid foundations and so on. With experience in soft and hard landscape installation and construction, we know that longevity is impacted by solid preparations.</p>
      <p>The Halvorsen group manages all excavation and site preparation works for you.</p>
    </section>

    <section class="panel panel--install">
      <h2 class="section-title">Installation &amp; Construction</h2>
      <p>Upon a well prepared site, The Halvorsen group are a professional landscape and construction company that works with a whole range of materials and structural designs.</p>
      <p>Browse through our portfolio to see our quality finishes and versatile capabilities including:</p>
      <div class="capabilities">
        <ul>
          <li>Decking</li>
          <li>Tiling</li>
          <li>Paving</li>
          <li>Pathways</li>
          <li>Irrigation</li>
          <li>Lawn</li>
          <li>Lighting</li>
          <li>Concreting</li>
          <li>Irrigation and Automatic Systems</li>
        </ul>
        <ul>
          <li>Walls and Screening</li>
          <li>Plant supply &amp; Installation</li>
          <li>Covered Structures and Arbours</li>
          <li>Water Features</li>
          <li>Rock features</li>
          <li>Aggregate designs</li>
          <li>Metal Sculptures</li>
          <li>Pool Paving and Features</li>
        </ul>
      </div>
      <p>Just some of the materials we have worked with include Bluestone, Limestone, Hardwood, Aggregate.</p>
    </section>

    <h2 class="headline headline--bottom">Landscaping to Your Lifestyle</h2>

    <div class="photo photo--entry" role="img" aria-label="Grand rendered entry with timber doors and garden lighting" style="left:0;top:598px;width:180px;height:166px;"></div>
    <div class="photo photo--pool" role="img" aria-label="Swimming pool with pale paving and lounge chair" style="left:180px;top:598px;width:180px;height:166px;"></div>
    <div class="photo photo--deck" role="img" aria-label="Timber deck steps beside rendered garden beds" style="left:360px;top:600px;width:180px;height:164px;"></div>
    <div class="photo photo--lawn" role="img" aria-label="Lawn with stepping stones and a garden screen" style="left:540px;top:600px;width:180px;height:164px;"></div>
    <div class="photo photo--garden-dusk" role="img" aria-label="Evening garden with lawn and stepping pavers" style="left:720px;top:600px;width:175px;height:164px;"></div>
    <div class="photo photo--timber" role="img" aria-label="Timber clad structure beside a paved courtyard" style="left:895px;top:600px;width:185px;height:164px;"></div>
  </main>
</body>
</html>
```